Anzeigengestaltung für Unternehmensberatung für Pflegedienste
Zielgruppe
Wir sind eine Unternehmensberatung für Pflegedienste. Es soll eine Werbeanzeige erstellt werden, mit welcher schlecht laufende Pflegedienste, die gerade in einer Krise stecken angesprochen werden,
Der slogan soll einfach klingen : Pflege neu gedaxht: wirtschaftlich, nachhaltig, zukunftssicher
Anzeige in 3 Formaten
1. Format 55.3 mm x 118 mm
2. Format 1/ halbe Seite Quer 176 x 118 mm un
3. Format d 1 x A4 _Seite
Der Name der Firma Keltor GmbH info at keltor.de Tel 0381 72958143 aus Rostock Berlin und bundesweit tätig
Aufgabenstellung
Kreativ und elegant

```html
<!DOCTYPE html>
<html lang="de">
<head>
<meta charset="utf-8">
<title>Keltor GmbH – Anzeigen</title>
<link href="https://fonts.googleapis.com/css2?family=Literata:opsz,wght@7..72,400;7..72,700&family=Hind:wght@400&display=swap" rel="stylesheet">
<style>
  :root {
    --stage: #c8c8c8;
    --paper: #ffffff;
    --navy: #15335e;
    --gold: #d4b068;
    --ink: #555555;
    --on-navy: #ffffff;
    --photo-skin: #efe3d8;
    --photo-scrub: #4e69bb;
  }
  * { box-sizing: border-box; margin: 0; padding: 0; }
  html, body { width: 1200px; height: 2323px; overflow: hidden; background: var(--stage); }
  body { position: relative; font-family: "Literata", Georgia, serif; }

  .ad { position: absolute; background: var(--paper); overflow: hidden; }
  .ad--tall { left: 284px; top: 112px; width: 633px; height: 1301px; }
  .ad--wide { left: 102px; top: 1513px; width: 997px; height: 666px; }

  .brand-name {
    position: absolute; z-index: 2; font-family: "Literata", Georgia, serif; font-weight: 400;
    color: var(--navy); line-height: 1; letter-spacing: 1px;
  }
  .ad--tall .brand-name { left: 0; right: 0; top: 64px; text-align: center; font-size: 70px; }
  .ad--wide .brand-name { left: 46px; top: 58px; font-size: 74px; }

  .slogan { position: absolute; z-index: 2; color: var(--ink); }
  .slogan__title { color: var(--navy); }
  .dot { display: inline-block; width: 12px; height: 12px; border-radius: 50%; background: var(--gold); margin-right: 6px; vertical-align: middle; }

  .ad--tall .slogan { left: 0; right: 0; top: 163px; text-align: center; font-size: 31px; line-height: 45px; white-space: nowrap; }
  .ad--tall .slogan__title { font-size: 32px; font-weight: 400; }
  .ad--tall .slogan .gap { display: inline-block; width: 10px; }

  .ad--wide .slogan { left: 46px; top: 198px; font-size: 35px; line-height: 54px; white-space: nowrap; }
  .ad--wide .slogan__title { font-size: 33px; font-weight: 700; }
  .ad--wide .slogan__item { padding-left: 4px; }

  .photo { position: absolute; z-index: 1; }
  .ad--tall .photo {
    left: 23px; top: 348px; width: 589px; height: 700px;
    background: linear-gradient(180deg, var(--paper) 0%, var(--photo-skin) 20%, #e6d2c1 40%, #6d84c6 60%, var(--photo-scrub) 100%);
  }
  .ad--wide .photo {
    left: 330px; top: 0; width: 667px; height: 575px;
    background:
      linear-gradient(90deg, var(--paper) 0%, rgba(255,255,255,0) 18%),
      linear-gradient(180deg, var(--paper) 0%, var(--photo-skin) 24%, #e6d2c1 44%, #6d84c6 64%, var(--photo-scrub) 100%);
  }

  .wave { position: absolute; z-index: 2; display: block; }
  .ad--tall .wave { left: 23px; top: 970px; width: 589px; height: 309px; }
  .ad--wide .wave { left: 0; top: 480px; width: 997px; height: 186px; }
  .wave__gold { fill: var(--gold); }
  .wave__navy { fill: var(--navy); }

  .footer { position: absolute; z-index: 3; color: var(--on-navy); font-family: "Hind", Arial, sans-serif; }
  .footer__company { font-family: "Literata", Georgia, serif; }
  .contacts { display: flex; align-items: center; font-family: "Hind", Arial, sans-serif; color: var(--on-navy); white-space: nowrap; }
  .contacts svg { fill: none; stroke: var(--on-navy); stroke-width: 1.6; flex: none; }
  .contacts .item { display: flex; align-items: center; }

  .ad--tall .footer { left: 23px; width: 589px; top: 1142px; text-align: center; }
  .ad--tall .footer__company { font-size: 31px; line-height: 40px; }
  .ad--tall .footer__region { font-size: 17px; line-height: 24px; margin-top: 4px; }
  .ad--tall .contacts { justify-content: center; gap: 14px; font-size: 17px; line-height: 24px; margin-top: 10px; }
  .ad--tall .contacts svg { width: 15px; height: 15px; }
  .ad--tall .contacts .item { gap: 6px; }

  .ad--wide .footer { left: 36px; top: 588px; font-size: 20px; line-height: 27px; }
  .ad--wide .footer__company { font-size: 19px; }
  .ad--wide .contacts { position: absolute; z-index: 3; left: 407px; top: 613px; font-size: 21px; gap: 22px; }
  .ad--wide .contacts svg { width: 22px; height: 22px; }
  .ad--wide .contacts .item { gap: 10px; }
</style>
</head>
<body>

<section class="ad ad--tall" aria-label="Anzeige Hochformat">
  <div class="brand-name">Keltor</div>
  <div class="slogan">
    <div class="slogan__title">Pflege neu gedaxht:</div>
    <div><span class="dot"></span>wirtschaftlich<span class="gap"></span> <span class="dot"></span>nachhaltig</div>
    <div><span class="dot"></span>zukunftssicher</div>
  </div>
  <div class="photo" role="img" aria-label="Foto: zwei lächelnde Pflegekräfte in blauer Dienstkleidung mit verschränkten Armen"></div>
  <svg class="wave" viewBox="0 0 589 309" preserveAspectRatio="none" aria-hidden="true">
    <path class="wave__gold" d="M0,0 Q300,75 589,20 L589,80 Q300,100 0,5 Z"/>
    <path class="wave__navy" d="M0,5 Q300,100 589,80 L589,309 L0,309 Z"/>
  </svg>
  <div class="footer">
    <div class="footer__company">Keltor GmbH</div>
    <div class="footer__region">Rostock, Berlin &amp; bundesweit tätig</div>
    <div class="contacts">
      <span class="item"><svg viewBox="0 0 20 20"><path d="M5 2 L8 6 L6.5 8 Q8 12 12 13.5 L14 12 L18 15 L16 18 Q9 18 5 13 Q2 9 2 4 Z"/></svg>0381 72958143</span>
      <span class="item"><svg viewBox="0 0 20 20"><rect x="2" y="5" width="16" height="11"/><path d="M2 5 L10 11 L18 5"/></svg>info@keltor.de</span>
      <span class="item"><svg viewBox="0 0 20 20"><circle cx="10" cy="10" r="8"/><ellipse cx="10" cy="10" rx="3.5" ry="8"/><path d="M2 10 H18 M3.5 6 H16.5 M3.5 14 H16.5"/></svg>www.keltor.de</span>
    </div>
  </div>
</section>

<section class="ad ad--wide" aria-label="Anzeige Querformat">
  <div class="photo" role="img" aria-label="Foto: zwei lächelnde Pflegekräfte in blauer Dienstkleidung mit verschränkten Armen"></div>
  <div class="brand-name">Keltor</div>
  <div class="slogan">
    <div class="slogan__title">Pflege neu gedaxht:</div>
    <div class="slogan__item"><span class="dot"></span>wirtschaftlich</div>
    <div class="slogan__item"><span class="dot"></span> nachhaltig</div>
    <div class="slogan__item"><span class="dot"></span>zukunftssicher</div>
  </div>
  <svg class="wave" viewBox="0 0 997 186" preserveAspectRatio="none" aria-hidden="true">
    <path class="wave__gold" d="M0,40 Q500,110 997,8 L997,45 Q500,125 0,48 Z"/>
    <path class="wave__navy" d="M0,48 Q500,125 997,45 L997,186 L0,186 Z"/>
  </svg>
  <div class="footer">
    <div class="footer__company">Keltor GmbH</div>
    <div class="footer__region">Rostock, Berlin &amp; bundesweit tätig</div>
  </div>
  <div class="contacts">
    <span class="item"><svg viewBox="0 0 20 20"><path d="M5 2 L8 6 L6.5 8 Q8 12 12 13.5 L14 12 L18 15 L16 18 Q9 18 5 13 Q2 9 2 4 Z"/></svg>0381 72958143</span>
    <span class="item"><svg viewBox="0 0 20 20"><rect x="2" y="5" width="16" height="11"/><path d="M2 5 L10 11 L18 5"/></svg>info@keltor.de</span>
    <span class="item"><svg viewBox="0 0 20 20"><circle cx="10" cy="10" r="8"/><ellipse cx="10" cy="10" rx="3.5" ry="8"/><path d="M2 10 H18 M3.5 6 H16.5 M3.5 14 H16.5"/></svg>www.keltor.de</span>
  </div>
</section>

</body>
</html>
```